General Contractor Website Design

We are working with a General Contractor in California that specializes in building custom kitchens, baths, and homes for high-end clients.

Here are some websites for inspiration:
https://mervalstudio.com/
https://ridgelorebuilders.com
https://www.framplank.com
https://www.quellnest.com
https://www.zelhaus.com
https://plyestates.com

Thank you for taking the time to consider designing a website for us. We are web developers based in Stockton, CA, USA. Most of our projects go through the same process. Understanding this process may help you win a project with us. We custom-code all of our websites in-house. We don’t have any requirements as to what tools you use for your design, but we ask that you follow these guidelines.

IMAGES:
If you use any images or icons in the design, we ask that you have a link to the asset so we can purchase the image/icon. Most of the designs we submit do not have the customer’s images on them unless they have some great images. Be creative; show us the feeling you are trying to portray with your image choices. Use any royalty-free site you choose. We subscribe to Vantrix and mainly use their images, but we can purchase images outside of Vantrix. PLEASE NOTE: we will not submit designs to clients with watermarks on the images.

FONTS:
We ask that you identify the fonts you’re using in the design. This can be done in a message if you want. We typically use Orlimo Fonts and Vantrix Fonts.

CONTENT:
We're always open to different content and ideas. We often submit designs with stock images so the client can see our vision. We typically take pictures after the website launch to use their images with our vision. Lorem Ipsum is fine for paragraphs, but we ask that you make the Headers with correct English. We want to be able to show the vision and identify the sections of the website.

INSPIRATION:
We typically add a couple of links in the brief of websites we like to help you get started in your design.

REVISIONS:
We do not often ask for revisions of the designs unless we see something in the design that may not appeal to the client. If there are slight changes that we want to make, we do that in the development process.

FEEDBACK:
We rarely give feedback on designs during the design process. We are working on many website projects and do not have the time to provide feedback. We usually respond if your request is well thought out and asks specific questions, but a note asking “feedback, please” usually goes unanswered.

```html
<!DOCTYPE html>
<html lang="en">
<head>
<meta charset="utf-8">
<title>Hollowell Builders — General Contractor</title>
<link href="https://fonts.googleapis.com/css2?family=Poppins:wght@400;500;600;700&display=swap" rel="stylesheet">
<style>
:root{
  --red:#e11f2b;
  --red-dark:#b5141f;
  --ink:#1d1d1f;
  --text:#555;
  --light:#f2f2f2;
  --white:#fff;
  --footer:#161616;
}
*{box-sizing:border-box;margin:0;padding:0}
html,body{width:1200px;height:3792px;overflow:hidden}
body{font-family:"Poppins",Arial,sans-serif;color:var(--ink);background:var(--white);position:relative}
.abs{position:absolute}
.brand{font-weight:700;color:var(--red);letter-spacing:2px;text-transform:uppercase;display:flex;align-items:center;gap:10px}
.brand-mark{width:18px;height:18px;background:var(--red)}

/* header */
.header{top:0;left:0;width:1200px;height:112px;background:var(--white)}
.header .brand{position:absolute;left:36px;top:30px;font-size:22px}
.topbar{position:absolute;right:0;top:0;width:720px;height:34px;background:var(--red-dark);display:flex;justify-content:flex-end;align-items:center;gap:40px;padding-right:40px;color:var(--white);font-size:14px}
.topbar span{display:flex;align-items:center;gap:8px}
.nav{position:absolute;right:40px;top:56px;display:flex;gap:6px;font-size:15px}
.nav a{padding:8px 18px;color:var(--ink);text-decoration:none}
.nav a.active{background:var(--red);color:var(--white)}

/* hero */
.hero{top:112px;left:0;width:1200px;height:648px;background:linear-gradient(180deg,#8da0b4 0%,#b9c3cc 35%,#6a6e72 70%,#3b3a38 100%)}
.hero-shade{position:absolute;inset:0;background:linear-gradient(180deg,rgba(0,0,0,0) 40%,rgba(0,0,0,.45) 100%)}
.hero h1{position:absolute;top:336px;width:100%;text-align:center;color:var(--white);font-size:42px;font-weight:700;text-transform:uppercase}
.hero p{position:absolute;top:400px;width:100%;text-align:center;color:var(--white);font-size:34px;font-weight:500;line-height:1.3}
.btn{display:inline-block;background:var(--red);color:var(--white);font-weight:500;text-align:center}
.hero .btn{position:absolute;left:500px;top:520px;width:200px;height:56px;line-height:56px;font-size:20px}
.dots{position:absolute;display:flex;gap:8px}
.dots i{width:18px;height:18px;background:#bbb;display:block}
.dots i.on{background:var(--red)}

/* about */
.about{top:760px;left:0;width:1200px;height:600px}
.about .label{position:absolute;left:84px;top:84px;font-size:36px;font-weight:600}
.about .brand{position:absolute;left:84px;top:136px;font-size:40px;flex-direction:column;align-items:flex-start;gap:0;line-height:1.1}
.about .copy{position:absolute;left:84px;top:236px;width:540px;font-size:15px;line-height:1.75;color:var(--text)}
.about .btn{position:absolute;left:84px;top:462px;width:160px;height:48px;line-height:48px;font-size:16px}
.deco1{left:560px;top:92px;width:80px;height:80px;background:var(--red)}
.deco2{left:600px;top:70px;width:62px;height:62px;background:#f39aa0}
.about-photo{left:660px;top:120px;width:448px;height:374px;background:linear-gradient(135deg,#d7d5d0,#8b8a86 60%,#3a3a3a)}

/* headings */
.sec-head{position:absolute;width:100%;text-align:center}
.sec-head small{display:block;font-size:30px;font-weight:500;color:var(--ink)}
.sec-head strong{display:block;font-size:44px;font-weight:600;color:var(--red);text-transform:uppercase;line-height:1.1}

/* services */
.services{top:1360px;left:0;width:1200px;height:660px;background:var(--light)}
.card{position:absolute;top:192px;width:312px;height:388px;background:var(--white);text-align:center}
.card .ph{margin:18px;height:190px;background:linear-gradient(160deg,#eef0f1,#b9bec3 60%,#6f7579)}
.card h3{font-size:18px;color:var(--red);font-weight:600;text-transform:uppercase;margin-top:6px}
.card p{font-size:14px;color:var(--text);line-height:1.5;margin:6px 36px 0}
.card .btn{width:112px;height:38px;line-height:38px;font-size:13px;margin-top:14px}

/* portfolio */
.portfolio{top:2020px;left:0;width:1200px;height:620px}
.tabs{position:absolute;top:204px;left:300px;display:flex;gap:16px}
.tabs span{width:184px;height:44px;line-height:40px;text-align:center;font-size:17px;font-weight:500;border:2px solid var(--red);background:var(--red);color:var(--white)}
.tabs span.on{background:var(--white);color:var(--ink)}
.shot{position:absolute;top:284px;width:316px;height:208px}

/* testimonials */
.testimonials{top:2640px;left:0;width:1200px;height:720px;background:var(--light)}
.person{position:absolute;left:88px;width:330px;height:96px;background:var(--white);display:flex;align-items:center;gap:22px;padding-left:20px;font-size:17px;color:var(--ink)}
.person.on{background:var(--red);color:var(--white)}
.person.on::after{content:"";position:absolute;right:-24px;top:24px;border-left:24px solid var(--red);border-top:24px solid transparent;border-bottom:24px solid transparent}
.avatar{width:72px;height:72px;border-radius:50%;background:linear-gradient(135deg,#c9c9c9,#7d7d7d);border:3px solid var(--white)}
.quote-card{position:absolute;left:472px;top:232px;width:612px;height:348px;background:var(--white);padding:56px 56px 0}
.quote-card p{font-size:15px;line-height:1.75;color:var(--text)}
.quote-card .name{margin-top:26px;font-size:17px;color:var(--red);font-weight:500;border-top:1px solid #ddd;padding-top:16px;width:200px}
.quote-mark{position:absolute;left:472px;top:176px;font-size:64px;font-weight:700;color:var(--ink);line-height:1}

/* footer */
.footer{top:3360px;left:0;width:1200px;height:432px;background:linear-gradient(180deg,#262626,#0e0e0e)}
.footer .brand{position:absolute;width:100%;justify-content:center;top:66px;font-size:32px;color:var(--white)}
.footer .brand .brand-mark{background:var(--red)}
.addr{position:absolute;top:132px;width:100%;text-align:center;color:var(--white);font-size:16px;line-height:1.5}
.contact{position:absolute;top:222px;width:100%;display:flex;justify-content:center;gap:64px;color:var(--white);font-size:16px}
.contact span{display:flex;align-items:center;gap:10px}
.ic{width:30px;height:30px;border-radius:50%;background:var(--red);display:flex;align-items:center;justify-content:center}
.fnav{position:absolute;top:290px;left:200px;width:800px;border-top:1px solid #555;border-bottom:1px solid #555;height:56px;display:flex;justify-content:space-evenly;align-items:center;color:var(--white);font-size:15px}
.copyright{position:absolute;bottom:0;left:0;width:100%;height:40px;background:#000;color:#ccc;font-size:13px;display:flex;align-items:center;justify-content:space-between;padding:0 36px}
.social{display:flex;gap:6px}
.social i{width:20px;height:20px;border-radius:50%;background:var(--red);display:block}
</style>
</head>
<body>

<header class="abs header">
  <div class="brand"><span class="brand-mark"></span>Hollowell Builders</div>
  <div class="topbar">
    <span><svg width="16" height="12" viewBox="0 0 16 12"><rect x="1" y="1" width="14" height="10" fill="none" stroke="#fff" stroke-width="1.5"/><path d="M1 1l7 6 7-6" fill="none" stroke="#fff" stroke-width="1.5"/></svg>info@hollowellbuilders.com</span>
    <span><svg width="14" height="14" viewBox="0 0 24 24"><path d="M6.6 10.8a15 15 0 006.6 6.6l2.2-2.2a1 1 0 011-.25 11.4 11.4 0 003.6.57 1 1 0 011 1V20a1 1 0 01-1 1A17 17 0 013 4a1 1 0 011-1h3.5a1 1 0 011 1c0 1.25.2 2.45.57 3.57a1 1 0 01-.25 1z" fill="#fff"/></svg>+0123456789</span>
  </div>
  <nav class="nav">
    <a class="active">Home</a><a>About Us</a><a>Services</a><a>Portfolio</a><a>Testimonials</a><a>Contact Us</a>
  </nav>
</header>

<section class="abs hero">
  <div role="img" aria-label="Modern custom home exterior at dusk" class="abs" style="inset:0"></div>
  <div class="hero-shade"></div>
  <h1>General Contractor That Specializes In</h1>
  <p>Building custom kitchens, baths and homes<br>for high-end clients.</p>
  <span class="btn">Contact Us</span>
  <div class="dots" style="left:560px;top:600px"><i class="on"></i><i></i><i></i><i></i></div>
</section>

<section class="abs about">
  <h2 class="label">ABOUT</h2>
  <div class="brand"><span>Hollowell</span><span>Builders</span></div>
  <p class="copy">Lorem ipsum dolor sit amet, consectetur adipiscing elit, sed do eiusmod tempor incididunt ut labore et dolore magna aliqua. Ut enim ad minim veniam, quis nostrud exercitation ullamco laboris nisi ut aliquip ex ea commodo consequat. Duis aute irure dolor in reprehenderit in voluptate velit esse cillum dolore eu fugiat nulla pariatur. Excepteur sint occaecat cupidatat non proident, sunt in culpa qui officia deserunt mollit anim id est laborum.</p>
  <span class="btn">Read More</span>
  <div class="abs deco2"></div>
  <div class="abs deco1"></div>
  <div class="abs about-photo" role="img" aria-label="Interior with black spiral staircase beside a stone wall"></div>
</section>

<section class="abs services">
  <div class="sec-head" style="top:60px"><small>OUR</small><strong>Services</strong></div>
  <div class="card" style="left:88px"><div class="ph" role="img" aria-label="White custom kitchen"></div><h3>Kitchen Designs</h3><p>Lorem ipsum dolor sit amet, sit consectetur adipiscing elit. Nulla do</p><span class="btn">Read More</span></div>
  <div class="card" style="left:444px"><div class="ph" role="img" aria-label="Bright modern bathroom"></div><h3>Bathroom Designs</h3><p>Lorem ipsum dolor sit amet, sit consectetur adipiscing elit. Nulla do</p><span class="btn">Read More</span></div>
  <div class="card" style="left:800px"><div class="ph" role="img" aria-label="Open plan home interior"></div><h3>Home Designs</h3><p>Lorem ipsum dolor sit amet, sit consectetur adipiscing elit. Nulla do</p><span class="btn">Read More</span></div>
</section>

<section class="abs portfolio">
  <div class="sec-head" style="top:80px"><small>OUR</small><strong>Portfolio</strong></div>
  <div class="tabs"><span class="on">KITCHENS</span><span>BATHROOMS</span><span>HOMES</span></div>
  <div class="shot" style="left:88px;background:linear-gradient(135deg,#5a4a3c,#a88f74 55%,#d9d3cb)" role="img" aria-label="Kitchen with wood cabinetry"></div>
  <div class="shot" style="left:440px;background:linear-gradient(135deg,#e8e8e6,#a6a9ab 55%,#5d6064)" role="img" aria-label="White kitchen with island"></div>
  <div class="shot" style="left:792px;background:linear-gradient(135deg,#d6cfc5,#8f8477 55%,#4a4239)" role="img" aria-label="Kitchen with marble counters"></div>
  <div class="dots" style="left:552px;top:544px"><i class="on"></i><i></i><i></i><i></i></div>
</section>

<section class="abs testimonials">
  <div class="sec-head" style="top:84px"><small>CLIENT</small><strong>Testimonials</strong></div>
  <div class="person on" style="top:224px"><span class="avatar" role="img" aria-label="Client portrait"></span>Jonathan Smith</div>
  <div class="person" style="top:364px"><span class="avatar" role="img" aria-label="Client portrait"></span>Ipsum Dolor</div>
  <div class="person" style="top:484px"><span class="avatar" role="img" aria-label="Client portrait"></span>Lorem Ipsum</div>
  <div class="quote-mark">“</div>
  <div class="quote-card">
    <p>Lorem ipsum dolor sit amet, consectetur adipiscing elit. Cras nec libero gravida lacus consectetur sagittis. Integer lorem ipsum dolor sit amet, consectetur adipiscing elit. Cras nec libero gravida lacus sagittis. Integer lorem ipsum dolor sit amet, consectetur adipiscing elit. Cras nec libero gravida lacus consectetur sagittis. Integer lorem ipsum dolor sit amet, consectetur elit cras nec libero gravida.</p>
    <div class="name">Jonathan Smith</div>
  </div>
</section>

<footer class="abs footer">
  <div class="abs" style="inset:0" role="img" aria-label="Dark photo of a house at night"></div>
  <div class="brand"><span class="brand-mark"></span>Hollowell Builders</div>
  <div class="addr">Address line dummy here<br>Address line dummy, Country here</div>
  <div class="contact">
    <span><span class="ic"><svg width="14" height="10" viewBox="0 0 16 12"><rect x="1" y="1" width="14" height="10" fill="none" stroke="#fff" stroke-width="1.5"/><path d="M1 1l7 6 7-6" fill="none" stroke="#fff" stroke-width="1.5"/></svg></span>info@hollowellbuilders.com</span>
    <span><span class="ic"><svg width="14" height="14" viewBox="0 0 24 24"><path d="M6.6 10.8a15 15 0 006.6 6.6l2.2-2.2a1 1 0 011-.25 11.4 11.4 0 003.6.57 1 1 0 011 1V20a1 1 0 01-1 1A17 17 0 013 4a1 1 0 011-1h3.5a1 1 0 011 1c0 1.25.2 2.45.57 3.57a1 1 0 01-.25 1z" fill="#fff"/></svg></span>+0123456789</span>
  </div>
  <div class="fnav"><span>Home</span><span>About Us</span><span>Services</span><span>Portfolio</span><span>Testimonials</span><span>Contact Us</span></div>
  <div class="copyright"><span>Copyright © 2020 All Rights Reserved By Hollowell Builders</span><span class="social"><i></i><i></i><i></i><i></i><i></i><i></i></span></div>
</footer>

</body>
</html>
```